Offshore Energy Projects Management Consultancy needs a business card design

Logo available. We provide teams to deliver engineering consultancy, project management and delivery teams mainly in the offshore renewables sector. The company is all about bringing the right people to a project to deliver the scope.

The business card will be used for all staff.

The business card should be quite simple, vibrant and uncluttered but convey experience, enthusiasm and integration.

Target Market(s)

Energy Project Developers and Tier 1 construction companies

Contact Information for Business Card

Logo should be on the back of the card. I'm happy for the designer to play with the colour of the logo and background colour.

Front of the card should convey all the must have information in a clear and professional manner but without being overly traditional.

Colors

Designer to choose colors to be used in the design.

Requirements
Must have
• Land Line Tel Number, Mobile Tel Number, Email, business address, web address.

```html
<!DOCTYPE html>
<html lang="en">
<head>
<meta charset="UTF-8">
<title>Tidewell Project Partners – Business Card</title>
<link href="https://fonts.googleapis.com/css2?family=Kanit:wght@300;400;500;600&display=swap" rel="stylesheet">
<style>
  :root {
    --bg: #c9ccd0;
    --brand-blue: #0a59a8;
    --bright-blue: #2a8fd6;
    --card-white: #f2f3f3;
    --ink: #1f2328;
    --slate: #6a6d70;
    --white: #ffffff;
  }
  * { margin: 0; padding: 0; box-sizing: border-box; }
  html, body {
    width: 1200px; height: 884px; overflow: hidden;
    background: var(--bg);
    font-family: "Kanit", sans-serif;
  }
  .canvas { position: relative; width: 1200px; height: 884px; }
  .card {
    position: absolute; top: 103px;
    width: 402px; height: 682px;
    border-radius: 38px;
  }
  .card-back { left: 147px; background: var(--brand-blue); }
  .card-front { left: 653px; background: var(--card-white); }
  .row {
    position: absolute; left: 0; width: 100%;
    text-align: center; white-space: nowrap;
  }
  .brand-name {
    font-weight: 600; letter-spacing: 0.5px; line-height: 1.1;
  }
  .card-back .brand-name { top: 350px; font-size: 31px; color: var(--white); }
  .card-back .brand-name span { display: block; }
  .card-back .site {
    top: 623px; font-size: 18px; font-weight: 300;
    letter-spacing: 2.5px; color: var(--white);
  }
  .card-front .brand-name { top: 178px; font-size: 26px; color: var(--slate); }
  .card-front .brand-name span { display: block; }
  .person-name {
    top: 302px; font-size: 30px; font-weight: 600; letter-spacing: 1px;
    color: var(--brand-blue);
  }
  .person-name .surname { color: var(--bright-blue); }
  .person-title { top: 339px; font-size: 18px; font-weight: 300; color: var(--ink); }
  .contact-icons {
    top: 400px; display: flex; justify-content: center; gap: 14px;
  }
  .contact-icons svg { width: 30px; height: 30px; }
  .phone { top: 438px; font-size: 22px; font-weight: 500; color: var(--brand-blue); letter-spacing: 0.5px; }
  .email { top: 469px; font-size: 18px; font-weight: 300; color: var(--ink); letter-spacing: 0.5px; }
  .web { top: 496px; font-size: 18px; font-weight: 300; color: var(--ink); letter-spacing: 0.5px; }
  .web .domain { color: var(--brand-blue); }
  .pin { top: 553px; }
  .pin svg { width: 30px; height: 30px; }
  .address { top: 592px; font-size: 18px; font-weight: 300; color: var(--ink); line-height: 26px; letter-spacing: 0.3px; }
</style>
</head>
<body>
<div class="canvas">

  <section class="card card-back">
    <div class="row brand-name"><span>TIDEWELL</span><span>PROJECT PARTNERS</span></div>
    <div class="row site">www.yourweb.com</div>
  </section>

  <section class="card card-front">
    <div class="row brand-name"><span>TIDEWELL</span><span>PROJECT PARTNERS</span></div>

    <div class="row person-name">MARTIN <span class="surname">HALE</span></div>
    <div class="row person-title">Founder &amp; CEO</div>

    <div class="row contact-icons">
      <svg viewBox="0 0 30 30" aria-label="Phone">
        <circle cx="15" cy="15" r="15" fill="var(--brand-blue)"/>
        <path d="M10 8.5c1-.6 1.8-.4 2.3.5l1 2c.3.7.1 1.3-.5 1.7l-.8.5c.6 1.6 1.8 2.9 3.4 3.6l.5-.8c.4-.6 1-.8 1.7-.5l2 1c.9.5 1.1 1.3.5 2.3-.8 1.2-2.1 1.6-3.5 1.1-3.3-1.2-5.7-3.6-6.9-6.9-.5-1.4-.1-2.7 1.1-3.5z" fill="#fff"/>
      </svg>
      <svg viewBox="0 0 30 30" aria-label="Email">
        <circle cx="15" cy="15" r="15" fill="var(--brand-blue)"/>
        <rect x="8" y="10" width="14" height="10" rx="1.5" fill="#fff"/>
        <path d="M8.5 10.8 15 15.6l6.5-4.8" fill="none" stroke="var(--brand-blue)" stroke-width="1.3"/>
      </svg>
      <svg viewBox="0 0 30 30" aria-label="Website">
        <circle cx="15" cy="15" r="15" fill="var(--brand-blue)"/>
        <g fill="none" stroke="#fff" stroke-width="1.3">
          <circle cx="15" cy="15" r="7"/>
          <ellipse cx="15" cy="15" rx="3" ry="7"/>
          <path d="M8 15h14M9 11.5h12M9 18.5h12"/>
        </g>
      </svg>
    </div>

    <div class="row phone">555.210.4837</div>
    <div class="row email">martin@yourmail.com</div>
    <div class="row web">www.<span class="domain">yourweb</span>.com</div>

    <div class="row pin">
      <svg viewBox="0 0 30 30" aria-label="Address">
        <path d="M15 3a6 6 0 0 0-6 6c0 4.5 6 11 6 11s6-6.5 6-11a6 6 0 0 0-6-6z" fill="var(--brand-blue)"/>
        <circle cx="15" cy="9" r="2.2" fill="#fff"/>
        <path d="M10 19.5c-4 .8-5.5 2.2-4 3.6 2 1.8 16 1.8 18 0 1.5-1.4 0-2.8-4-3.6" fill="none" stroke="var(--brand-blue)" stroke-width="1.6"/>
      </svg>
    </div>

    <div class="row address">1840 Harbor Crest Rd. Ste. 300,<br>Norfolk, VA 23510-1120</div>
  </section>

</div>
</body>
</html>
```